Business Postcard Mailer - 2 sided - 6 x 10.5 inches

We will be purchasing multiple designs through this project. We need a postcard mailer for a residential painting business. The final design needs to have the special 15% Off, contact information, company logo, stamp indicia, and list of services. I will provide past examples and any additional logos. Company colors are #34482E and #4A1717. Old samples are provided. Final flat size should be 6 x 10.5 inches. And we will need a return address in the upper left-hand corner of the backside. QMRB Layout Guidelines are attached. 4389 Juniper Ave #7, Waukesha, WI 53947.
Updates

I just guaranteed the project and will be expecting more entries. We will also be purchasing additional designs (4-5) so we want to ensure a good variety.

Target Market(s)

Homeowners

Industry/Entity Type

Painting

Font styles to use
Sans Serif

Requirements
Must have
• Logo and brand colors
Nice to have
• Call to action - Book your free estimate at www.BrightCoatCrew.example or Call now 262-555-0147.

```html
<!DOCTYPE html>
<html lang="en">
<head>
<meta charset="utf-8">
<title>Bright Coat Crew – Spring Postcard Mailer</title>
<link rel="stylesheet" href="https://fonts.googleapis.com/css2?family=Archivo+Black&family=Montserrat:wght@500;600;700;800&family=Oswald:wght@300;400&display=swap">
<style>
  :root {
    --green: #34482E;
    --maroon: #4A1717;
    --white: #ffffff;
    --paper: #f4f4f2;
    --stage: #e4e5e6;
    --grey: #b9bcbd;
  }
  * { box-sizing: border-box; margin: 0; padding: 0; }
  html, body { width: 953px; height: 1200px; overflow: hidden; }
  body { background: var(--stage); font-family: "Montserrat", sans-serif; position: relative; }

  .card { position: absolute; left: 20px; width: 913px; height: 522px; overflow: hidden; background: var(--white); box-shadow: 0 4px 10px rgba(0,0,0,.25); }
  .card--front { top: 60px; }
  .card--back { top: 617px; }
  .layer { position: absolute; }

  /* FRONT */
  .hero-photo { left: 0; top: 0; width: 913px; height: 290px; background: linear-gradient(180deg, #e9e8e3 0%, #d8d6cf 55%, #b9b3a7 100%); }
  .logo-plate { left: 0; top: 0; width: 300px; height: 140px; background: var(--paper); clip-path: polygon(0 0, 100% 0, 92% 100%, 0 100%); }
  .brand { position: absolute; left: 18px; top: 24px; display: flex; align-items: center; gap: 12px; color: var(--green); font-weight: 800; font-size: 31px; line-height: 1.05; }
  .brand-mark { width: 22px; height: 22px; background: var(--maroon); flex: none; }
  .headline-band { left: 0; top: 155px; width: 600px; height: 135px; background: rgba(255,255,255,.78); clip-path: polygon(0 0, 100% 0, 93% 100%, 0 100%); }
  .headline { position: absolute; left: 17px; top: 160px; }
  .headline-main { font-family: "Archivo Black", sans-serif; color: var(--green); font-size: 50px; line-height: 1; letter-spacing: 1px; }
  .headline-sub { font-family: "Oswald", sans-serif; font-weight: 400; color: var(--maroon); font-size: 44px; line-height: 1.2; letter-spacing: .5px; margin-top: 4px; }
  .ribbon { left: 752px; top: 0; width: 160px; height: 162px; }
  .ribbon-text { position: absolute; left: 752px; top: 6px; width: 160px; text-align: center; color: var(--white); }
  .ribbon-text .season { font-weight: 500; font-size: 25px; line-height: 1.1; }
  .ribbon-text .stars { font-size: 16px; letter-spacing: 8px; margin: 4px 0 2px 8px; }
  .ribbon-text .deal { font-weight: 800; font-size: 29px; }
  .cta-box { left: 588px; top: 175px; width: 325px; height: 93px; background: var(--green); border-radius: 16px 0 0 16px; color: var(--white); text-align: center; font-weight: 700; font-size: 16px; line-height: 1.6; padding-top: 10px; }

  .services-back { left: 0; top: 290px; width: 913px; height: 232px; background: var(--green); }
  .services-panel { left: 0; top: 290px; width: 466px; height: 232px; background: var(--white); clip-path: polygon(0 0, 100% 0, 90% 100%, 0 100%); }
  .services-title { left: 0; top: 290px; width: 205px; height: 34px; background: var(--green); clip-path: polygon(0 0, 100% 0, 90% 100%, 0 100%); color: var(--white); font-weight: 700; font-size: 18px; padding: 6px 0 0 16px; }
  .services-list { list-style: none; top: 344px; color: var(--green); font-weight: 600; font-size: 13px; }
  .services-list li { height: 20.2px; display: flex; align-items: center; gap: 6px; }
  .services-list svg { width: 10px; height: 10px; flex: none; }
  .services-list--one { left: 16px; }
  .services-list--two { left: 222px; }
  .contact-bar { left: 0; top: 472px; width: 416px; height: 50px; background: var(--maroon); clip-path: polygon(0 0, 100% 0, 96% 100%, 0 100%); color: var(--white); font-size: 13px; font-weight: 500; display: flex; align-items: center; gap: 8px; padding-left: 16px; white-space: nowrap; }
  .contact-bar svg { width: 14px; height: 14px; flex: none; }
  .contact-bar .sep { width: 4px; }
  .photo-circle { width: 216px; height: 216px; border-radius: 50%; border: 4px solid var(--white); top: 282px; }
  .photo-circle--one { left: 456px; background: radial-gradient(circle at 50% 40%, #c9d3dc 0%, #8c9aa3 45%, #4f6b3c 100%); }
  .photo-circle--two { left: 687px; background: radial-gradient(circle at 50% 40%, #eef0ee 0%, #8b93a0 50%, #6f7f4c 100%); }

  /* BACK */
  .back-green { left: 0; top: 0; width: 482px; height: 332px; background: var(--green); }
  .back-badges { left: 0; top: 332px; width: 474px; height: 147px; background: linear-gradient(180deg, #e9e9e7, #f6f6f4); }
  .divider { left: 0; top: 0; width: 913px; height: 522px; }
  .back-brand { position: absolute; left: 16px; top: 16px; display: flex; align-items: center; gap: 10px; color: var(--white); font-weight: 800; font-size: 21px; line-height: 1.05; }
  .back-brand .brand-mark { width: 16px; height: 16px; background: var(--white); }
  .return-address { left: 22px; top: 98px; color: var(--white); font-size: 14px; font-weight: 500; line-height: 1.5; }
  .back-cta { left: 188px; top: 36px; width: 286px; text-align: center; color: var(--white); font-weight: 700; font-size: 15px; line-height: 1.8; }
  .ba-photo { top: 153px; width: 213px; height: 129px; border: 7px solid var(--white); }
  .ba-photo--before { left: 16px; background: linear-gradient(180deg, #b9c6cf 0%, #dcdcd8 50%, #7a8a5c 100%); }
  .ba-photo--after { left: 237px; background: linear-gradient(180deg, #b7c5cf 0%, #55606a 50%, #6e824d 100%); }
  .ba-label { top: 295px; width: 213px; text-align: center; color: var(--white); font-weight: 600; font-size: 15px; }
  .ba-label--before { left: 16px; }
  .ba-label--after { left: 237px; }
  .badge { background: var(--grey); opacity: .55; }
  .badge--round { border-radius: 50%; }
  .back-bar { left: 0; top: 479px; width: 474px; height: 43px; background: var(--maroon); color: var(--white); font-weight: 600; font-size: 15px; letter-spacing: 6.3px; padding: 11px 0 0 16px; white-space: nowrap; }
  .indicia { left: 816px; top: 16px; width: 77px; height: 78px; border: 1.5px solid #222; text-align: center; font-size: 9px; line-height: 1.3; color: #111; padding-top: 4px; }
  .indicia .paid { font-weight: 700; font-size: 12px; border-top: 1px solid #222; border-bottom: 1px solid #222; margin: 2px 4px; }
</style>
</head>
<body>

<section class="card card--front" aria-label="Postcard front">
  <div class="layer hero-photo" role="img" aria-label="Photo of a bright white kitchen with pendant lights and cabinets"></div>
  <div class="layer logo-plate">
    <div class="brand"><span class="brand-mark"></span><span>Bright Coat<br>Crew</span></div>
  </div>
  <div class="layer headline-band"></div>
  <div class="headline">
    <div class="headline-main">LET THE PROS</div>
    <div class="headline-sub">TAKE CARE OF THE WORK</div>
  </div>

  <svg class="layer ribbon" viewBox="0 0 160 162" aria-hidden="true">
    <polygon points="0,0 160,0 160,162 80,138 0,162" fill="#4A1717"/>
    <polyline points="8,0 8,150 80,128 152,150 152,0" fill="none" stroke="#fff" stroke-width="1.5" stroke-dasharray="5 4"/>
  </svg>
  <div class="ribbon-text">
    <div class="season">Spring<br>Special</div>
    <div class="stars">★★★</div>
    <div class="deal">15% OFF</div>
  </div>

  <div class="layer cta-box">Book your free estimate<br>at www.BrightCoatCrew.example<br>or Call now 262-555-0147</div>

  <div class="layer services-back"></div>
  <div class="layer services-panel"></div>
  <div class="layer services-title">OUR SERVICES</div>
  <ul class="layer services-list services-list--one">
    <li><svg viewBox="0 0 10 10"><rect x=".5" y=".5" width="9" height="9" fill="none" stroke="#34482E"/><path d="M2 5l2 2 4-5" fill="none" stroke="#34482E" stroke-width="1.4"/></svg>INTERIOR PAINTING</li>
    <li><svg viewBox="0 0 10 10"><rect x=".5" y=".5" width="9" height="9" fill="none" stroke="#34482E"/><path d="M2 5l2 2 4-5" fill="none" stroke="#34482E" stroke-width="1.4"/></svg>EXTERIOR PAINTING</li>
    <li><svg viewBox="0 0 10 10"><rect x=".5" y=".5" width="9" height="9" fill="none" stroke="#34482E"/><path d="M2 5l2 2 4-5" fill="none" stroke="#34482E" stroke-width="1.4"/></svg>CARPENTRY SERVICES</li>
    <li><svg viewBox="0 0 10 10"><rect x=".5" y=".5" width="9" height="9" fill="none" stroke="#34482E"/><path d="M2 5l2 2 4-5" fill="none" stroke="#34482E" stroke-width="1.4"/></svg>DRYWALL REPAIR</li>
    <li><svg viewBox="0 0 10 10"><rect x=".5" y=".5" width="9" height="9" fill="none" stroke="#34482E"/><path d="M2 5l2 2 4-5" fill="none" stroke="#34482E" stroke-width="1.4"/></svg>COLOR CONSULTATIONS</li>
    <li><svg viewBox="0 0 10 10"><rect x=".5" y=".5" width="9" height="9" fill="none" stroke="#34482E"/><path d="M2 5l2 2 4-5" fill="none" stroke="#34482E" stroke-width="1.4"/></svg>DECKS &amp; FENCES</li>
  </ul>
  <ul class="layer services-list services-list--two">
    <li><svg viewBox="0 0 10 10"><rect x=".5" y=".5" width="9" height="9" fill="none" stroke="#34482E"/><path d="M2 5l2 2 4-5" fill="none" stroke="#34482E" stroke-width="1.4"/></svg>KITCHEN CABINETS</li>
    <li><svg viewBox="0 0 10 10"><rect x=".5" y=".5" width="9" height="9" fill="none" stroke="#34482E"/><path d="M2 5l2 2 4-5" fill="none" stroke="#34482E" stroke-width="1.4"/></svg>SIDING AND TRIM REPAIR</li>
    <li><svg viewBox="0 0 10 10"><rect x=".5" y=".5" width="9" height="9" fill="none" stroke="#34482E"/><path d="M2 5l2 2 4-5" fill="none" stroke="#34482E" stroke-width="1.4"/></svg>STAINING</li>
    <li><svg viewBox="0 0 10 10"><rect x=".5" y=".5" width="9" height="9" fill="none" stroke="#34482E"/><path d="M2 5l2 2 4-5" fill="none" stroke="#34482E" stroke-width="1.4"/></svg>POWER WASHING</li>
    <li><svg viewBox="0 0 10 10"><rect x=".5" y=".5" width="9" height="9" fill="none" stroke="#34482E"/><path d="M2 5l2 2 4-5" fill="none" stroke="#34482E" stroke-width="1.4"/></svg>PLASTER REPAIR</li>
    <li><svg viewBox="0 0 10 10"><rect x=".5" y=".5" width="9" height="9" fill="none" stroke="#34482E"/><path d="M2 5l2 2 4-5" fill="none" stroke="#34482E" stroke-width="1.4"/></svg>INTERIOR TRIM</li>
  </ul>

  <div class="layer contact-bar">
    <svg viewBox="0 0 16 16"><path d="M3 1l3 3-2 2c1 2 3 4 5 5l2-2 3 3-2 3C7 15 1 9 1 3z" fill="#fff"/></svg>
    <span>262-555-0147</span><span class="sep"></span>
    <svg viewBox="0 0 16 16"><g fill="none" stroke="#fff" stroke-width="1.2"><circle cx="8" cy="8" r="6.5"/><ellipse cx="8" cy="8" rx="3" ry="6.5"/><path d="M1.5 8h13M2.5 4.5h11M2.5 11.5h11"/></g></svg>
    <span>www.brightcoatcrew.example</span>
  </div>

  <div class="layer photo-circle photo-circle--one" role="img" aria-label="Photo of a large two-storey family home with white siding and green lawn"></div>
  <div class="layer photo-circle photo-circle--two" role="img" aria-label="Photo of a grey bungalow with a white front porch"></div>
</section>

<section class="card card--back" aria-label="Postcard back">
  <div class="layer back-green"></div>
  <div class="layer back-badges"></div>
  <svg class="layer divider" viewBox="0 0 913 522" aria-hidden="true">
    <polygon points="474,0 493,0 468,470 474,479 474,522 452,522 452,478 474,470" fill="#4A1717"/>
  </svg>

  <div class="back-brand"><span class="brand-mark"></span><span>Bright Coat<br>Crew</span></div>
  <div class="layer return-address">4389 Juniper Ave #7,<br>Waukesha, WI 53947</div>
  <div class="layer back-cta">Book your free estimate<br>at www.BrightCoatCrew.example<br>or Call now 262-555-0147</div>

  <div class="layer ba-photo ba-photo--before" role="img" aria-label="Photo of a farmhouse before painting, with ladders and bare siding"></div>
  <div class="layer ba-photo ba-photo--after" role="img" aria-label="Photo of the same farmhouse after painting in dark grey"></div>
  <div class="layer ba-label ba-label--before">BEFORE</div>
  <div class="layer ba-label ba-label--after">AFTER</div>

  <div class="layer badge badge--round" style="left:16px;top:348px;width:62px;height:62px"></div>
  <div class="layer badge" style="left:82px;top:354px;width:46px;height:46px"></div>
  <div class="layer badge" style="left:16px;top:420px;width:70px;height:42px"></div>
  <div class="layer badge badge--round" style="left:160px;top:346px;width:54px;height:54px"></div>
  <div class="layer badge" style="left:118px;top:420px;width:150px;height:38px"></div>
  <div class="layer badge" style="left:274px;top:358px;width:70px;height:34px"></div>
  <div class="layer badge" style="left:370px;top:350px;width:68px;height:50px"></div>
  <div class="layer badge" style="left:274px;top:416px;width:70px;height:50px"></div>

  <div class="layer back-bar">www.brightcoatcrew.example</div>

  <div class="layer indicia">Presorted<br>Standard<br>QMRB Postage<div class="paid">PAID</div>RPM</div>
</section>

</body>
</html>
```